Olive Oil Label Needs Graphic Designs

We need two sister label designs for 500ml bottles for our new brand "Casa Lumen". Casa Lumen is a high-end olive oil from Baeza, Spain which will be sold in the US. The oil will be produced from both Arbequina olives and Picual olives. Therefore, envisioning the same design just a different color scheme for the different labels.
The label should have the following characteristics; clean and simple, stand-out from mainstream labels, be eye-catching, give perception of high-end / high-quality.
Our current thinking of what we want (but please let your creative juices flow); lighter background, to be more eye catching, graphics of and olive, a olive branch or olive tree.
Text which should appear on the label are (not necessarily in this order);
Casa Lumen
Extra Virgin Olive Oil
Family Reserve
Arbequina (One design)
Picual (Second design)
The label should be about 3 inches wide and 5.5 inches in height.

```html
<!DOCTYPE html>
<html lang="en">
<head>
<meta charset="utf-8">
<title>Casa Lumen — Extra Virgin Olive Oil Labels</title>
<link href="https://fonts.googleapis.com/css2?family=Questrial&family=Libre+Baskerville:wght@400;700&display=swap" rel="stylesheet">
<style>
  :root {
    --canvas: #e4e5e6;
    --paper: #ffffff;
    --leaf-dark: #2f6a14;
    --leaf-deep: #255a0f;
    --leaf-light: #bfd96a;
    --leaf-mid: #7fa93a;
    --gold: #b98a3c;
    --gold-light: #e6c98a;
    --ink: #2b2b2b;
    --muted: #5a5a5a;
  }
  * { box-sizing: border-box; margin: 0; padding: 0; }
  html, body { width: 1200px; height: 1000px; overflow: hidden; }
  body {
    background: var(--canvas);
    font-family: "Questrial", "Helvetica Neue", sans-serif;
    color: var(--ink);
  }
  .label-set {
    display: flex;
    justify-content: center;
    gap: 75px;
    padding-top: 225px;
  }
  .label {
    position: relative;
    width: 300px;
    height: 550px;
    background: var(--paper);
    box-shadow: 0 2px 10px rgba(0,0,0,0.12);
  }
  .brand {
    position: absolute;
    top: 46px;
    left: 0; right: 0;
    display: flex;
    justify-content: center;
    align-items: center;
    gap: 8px;
    font-size: 22px;
    color: var(--leaf-dark);
    letter-spacing: 0.5px;
  }
  .brand-dot {
    width: 12px; height: 12px;
    border-radius: 50%;
    background: var(--leaf-dark);
  }
  .band {
    position: absolute;
    top: 145px;
    left: 0;
    width: 300px;
    height: 310px;
    display: block;
  }
  .label-foot {
    position: absolute;
    bottom: 22px;
    left: 24px; right: 24px;
    display: flex;
    justify-content: space-between;
    font-size: 11px;
    color: var(--muted);
  }

  /* back label */
  .back .rule {
    position: absolute; left: 0; right: 0; height: 3px;
    background: linear-gradient(90deg, var(--gold), var(--gold-light), var(--gold));
  }
  .back .rule.top { top: 8px; }
  .back .rule.bottom { bottom: 8px; }
  .back-title {
    position: absolute;
    top: 40px; left: 0; right: 0;
    text-align: center;
    color: var(--leaf-dark);
  }
  .back-title .kicker { font-size: 10px; letter-spacing: 2px; }
  .back-title .name { font-size: 26px; line-height: 1.15; letter-spacing: 1px; }
  .back-title .divider {
    width: 80px; height: 2px; margin: 8px auto 0;
    background: var(--gold);
  }
  .nutrition {
    position: absolute;
    top: 142px; left: 42px;
    width: 216px;
    border: 1px solid var(--leaf-dark);
    padding: 4px 6px;
    font-family: "Libre Baskerville", Georgia, serif;
    font-size: 7px;
    line-height: 1.45;
    color: var(--leaf-deep);
  }
  .nutrition h2 { font-size: 11px; text-align: center; line-height: 1.2; }
  .nutrition .serving { text-align: center; border-bottom: 4px solid var(--leaf-dark); padding-bottom: 2px; }
  .nutrition .row { display: flex; justify-content: space-between; border-bottom: 0.5px solid var(--leaf-dark); }
  .nutrition .row.indent { padding-left: 8px; }
  .nutrition .thick { border-bottom: 3px solid var(--leaf-dark); }
  .nutrition .note { padding-top: 2px; }
  .statement {
    position: absolute;
    top: 368px; left: 50px; width: 200px;
    font-family: "Libre Baskerville", Georgia, serif;
    font-size: 7px; line-height: 1.45;
    text-align: center; color: var(--leaf-deep);
  }
  .distributor {
    position: absolute;
    bottom: 36px; left: 0; right: 0;
    font-family: "Libre Baskerville", Georgia, serif;
    font-size: 7px; text-align: center; color: var(--leaf-deep);
  }
</style>
</head>
<body>
<main class="label-set">

  <!-- Arbequina front label -->
  <section class="label front arbequina">
    <div class="brand"><span class="brand-dot"></span><span>Casa Lumen</span></div>
    <svg class="band" viewBox="0 0 300 310" xmlns="http://www.w3.org/2000/svg">
      <defs>
        <linearGradient id="gold-a" x1="0" x2="1"><stop offset="0" stop-color="#b98a3c"/><stop offset="0.5" stop-color="#e6c98a"/><stop offset="1" stop-color="#b98a3c"/></linearGradient>
      </defs>
      <rect x="0" y="0" width="300" height="3" fill="url(#gold-a)"/>
      <rect x="0" y="3" width="300" height="281" fill="var(--leaf-light)"/>
      <rect role="img" aria-label="Olive branch with green olives and leaves" x="90" y="14" width="120" height="48" rx="6" fill="var(--leaf-mid)"/>
      <rect x="30" y="76" width="240" height="196" fill="none" stroke="var(--leaf-dark)" stroke-width="2"/>
      <g fill="var(--leaf-dark)" font-family="Questrial, sans-serif" text-anchor="middle">
        <text x="150" y="118" font-size="19" letter-spacing="2">EXTRA VIRGIN</text>
        <text x="150" y="180" font-size="50">OLIVE</text>
        <text x="150" y="244" font-size="50">OIL</text>
      </g>
      <rect x="0" y="284" width="300" height="22" fill="var(--leaf-dark)"/>
      <text x="150" y="301" text-anchor="middle" font-family="Questrial, sans-serif" font-size="15" fill="var(--leaf-light)">ARBEQUINA OLIVES</text>
      <rect x="0" y="306" width="300" height="3" fill="url(#gold-a)"/>
    </svg>
    <div class="label-foot"><span>Family Reserve</span><span>500ml</span></div>
  </section>

  <!-- Picual front label -->
  <section class="label front picual">
    <div class="brand"><span class="brand-dot"></span><span>Casa Lumen</span></div>
    <svg class="band" viewBox="0 0 300 310" xmlns="http://www.w3.org/2000/svg">
      <defs>
        <linearGradient id="gold-p" x1="0" x2="1"><stop offset="0" stop-color="#b98a3c"/><stop offset="0.5" stop-color="#e6c98a"/><stop offset="1" stop-color="#b98a3c"/></linearGradient>
      </defs>
      <rect x="0" y="0" width="300" height="3" fill="url(#gold-p)"/>
      <rect x="0" y="3" width="300" height="281" fill="var(--leaf-dark)"/>
      <rect role="img" aria-label="Olive branch with green olives and leaves" x="90" y="14" width="120" height="48" rx="6" fill="var(--leaf-mid)"/>
      <rect x="30" y="76" width="240" height="196" fill="none" stroke="var(--leaf-light)" stroke-width="2"/>
      <g fill="var(--leaf-light)" font-family="Questrial, sans-serif" text-anchor="middle">
        <text x="150" y="118" font-size="19" letter-spacing="2">EXTRA VIRGIN</text>
        <text x="150" y="180" font-size="50">OLIVE</text>
        <text x="150" y="244" font-size="50">OIL</text>
      </g>
      <rect x="0" y="284" width="300" height="22" fill="var(--leaf-light)"/>
      <text x="150" y="301" text-anchor="middle" font-family="Questrial, sans-serif" font-size="15" fill="var(--leaf-dark)">PICUAL OLIVES</text>
      <rect x="0" y="306" width="300" height="3" fill="url(#gold-p)"/>
    </svg>
    <div class="label-foot"><span>Family Reserve</span><span>500ml</span></div>
  </section>

  <!-- Back label -->
  <section class="label back">
    <div class="rule top"></div>
    <div class="back-title">
      <div class="kicker">EXTRA VIRGIN</div>
      <div class="name">OLIVE OIL</div>
      <div class="divider"></div>
    </div>
    <div class="nutrition">
      <h2>Nutrition Facts</h2>
      <div class="serving">Serving Size 1 Tbsp. 15ml<br>Servings Per Container 33</div>
      <div class="row">Amount Per Serving</div>
      <div class="row">Calories 120</div>
      <div class="row thick">Calories from Fat 120</div>
      <div class="row"><span></span><span>% Daily Value*</span></div>
      <div class="row"><span>Total Fat 14g</span><span>22%</span></div>
      <div class="row indent"><span>Saturated Fat 2g</span><span>10%</span></div>
      <div class="row indent"><span>Trans Fat 0g</span><span></span></div>
      <div class="row"><span>Cholesterol 0mg</span><span>0%</span></div>
      <div class="row"><span>Sodium 0mg</span><span>0%</span></div>
      <div class="row"><span>Total Carbohydrate 0g</span><span>0%</span></div>
      <div class="row indent"><span>Sugar 0g</span><span></span></div>
      <div class="row thick">Protein 0g</div>
      <div class="row note">Not a significant source of dietary fiber, Vitamin A, Vitamin C, Calcium or Iron.</div>
      <div class="note">* Percent Daily Values are based on a 2,000 calorie diet.</div>
    </div>
    <p class="statement">This product has been produced free from soy, wheat, gluten, nuts, peanuts, dairy, and genetically engineered ingredients.</p>
    <p class="distributor">Distributor Info</p>
    <div class="rule bottom"></div>
  </section>

</main>
</body>
</html>
```